Banner

I need a banner made showcasing our products and USPs! I have attached a design that was done in-house but not very good so looking for a better design

Industry/Entity Type

Fintech

```html
<!DOCTYPE html>
<html lang="en">
<head>
<meta charset="utf-8">
<title>Levelpay Merchant Services – Banner</title>
<link rel="stylesheet" href="https://fonts.googleapis.com/css2?family=Roboto:wght@400;500;700&display=swap">
<style>
  :root {
    --blue: #124c8c;
    --blue-text: #1a4f9a;
    --orange: #ee8a22;
    --ring: #6f73b4;
    --grey: #5a5a5a;
    --ink: #1f1f1f;
    --white: #ffffff;
    --sky: #8fb6e2;
    --stone: #4a433d;
    --brick: #c8623e;
  }
  * { box-sizing: border-box; margin: 0; padding: 0; }
  html, body { width: 1200px; height: 1200px; overflow: hidden; background: var(--white); }
  body { font-family: "Roboto", Arial, sans-serif; position: relative; }

  .banner {
    position: absolute; left: 315px; top: 30px;
    width: 698px; height: 1395px;
    transform: scale(0.817); transform-origin: 0 0;
    background: var(--white); overflow: hidden;
  }
  .banner > * { position: absolute; }
  .shapes { left: 0; top: 0; width: 698px; height: 1395px; }

  .brand { left: 0; width: 698px; top: 28px; text-align: center; }
  .brand-name { font-size: 82px; font-weight: 500; color: var(--blue-text); line-height: 1; letter-spacing: -1px; }
  .brand-sub { font-size: 20px; color: var(--grey); margin-top: 4px; letter-spacing: .5px; }

  .tagline { left: 349px; top: 146px; color: var(--grey); }
  .tagline .l1 { font-size: 28px; line-height: 34px; }
  .tagline .l2 { font-size: 28px; line-height: 34px; color: var(--ink); }
  .tagline .l2 b { font-weight: 700; color: var(--grey); }
  .tagline .l3 { font-size: 19px; color: var(--blue-text); margin-top: 12px; margin-left: 4px; letter-spacing: .3px; }

  .quote-badge {
    left: 44px; top: 272px; width: 188px; height: 188px; border-radius: 50%;
    background: var(--orange); border: 5px solid var(--ring);
    display: flex; flex-direction: column; align-items: center; justify-content: center;
    color: var(--ink); text-align: center; line-height: 1.25;
  }
  .quote-badge .small { font-size: 18px; }
  .quote-badge .big { font-size: 58px; line-height: 1; margin: 2px 0 4px; }

  .usp-list { left: 22px; top: 770px; width: 260px; list-style: none; }
  .usp {
    display: flex; align-items: center; gap: 10px;
    height: 80px; color: var(--white); font-size: 18px; line-height: 24px;
  }
  .usp + .usp { border-top: 2px solid rgba(255,255,255,.85); margin-left: 66px; padding-left: 0; }
  .usp + .usp .usp-icon { margin-left: -66px; }
  .usp-icon {
    flex: none; width: 56px; height: 56px; border-radius: 50%;
    background: var(--white); display: flex; align-items: center; justify-content: center;
  }
  .usp-icon svg { width: 34px; height: 34px; }

  .service {
    width: 192px; height: 192px; border-radius: 50%;
    background: var(--white); border: 7px solid var(--ring);
    display: flex; flex-direction: column; align-items: center; justify-content: flex-end;
    padding-bottom: 22px; text-align: center;
    color: var(--blue-text); font-weight: 700; font-size: 22px; line-height: 30px;
  }
  .service-art { width: 110px; height: 72px; border-radius: 8px; margin-bottom: 8px; }
  .service--epos { left: 306px; top: 899px; }
  .service--cash { left: 494px; top: 1026px; }
  .service--card { left: 306px; top: 1122px; }
  .art-epos { background: linear-gradient(160deg, #5a6b8c, #2b2b2f); }
  .art-cash { background: linear-gradient(160deg, #e4c6a8, #b2574a); }
  .art-card { background: linear-gradient(160deg, #c9cdd3, #5d6066); width: 70px; height: 80px; }

  .payment-row { left: 12px; top: 1354px; display: flex; gap: 6px; }
  .pay-mark { width: 44px; height: 26px; border-radius: 3px; border: 1px solid #bfbfbf; background: var(--white); }
  .pay-mark--round { border-radius: 50%; width: 48px; }
  .pay-mark--purple { background: #6a2a8a; border-color: #6a2a8a; }
  .pay-mark--red { background: #1a3a8a; border-color: #1a3a8a; }
</style>
</head>
<body>
<div class="banner">
  <svg class="shapes" viewBox="0 0 698 1395" aria-hidden="false">
    <defs>
      <linearGradient id="cityTones" x1="0" y1="1" x2="1" y2="0">
        <stop offset="0" stop-color="#3d3631"/>
        <stop offset="0.45" stop-color="#5a514a"/>
        <stop offset="0.62" stop-color="#b55a3a"/>
        <stop offset="0.8" stop-color="#7fa9dc"/>
        <stop offset="1" stop-color="#a9c8ec"/>
      </linearGradient>
    </defs>
    <polygon points="0,122 424,375 0,605" fill="var(--blue)"/>
    <polygon points="0,632 698,962 698,1395 470,1395 0,1148" fill="var(--blue)"/>
    <polygon points="698,254 0,628 698,962" fill="url(#cityTones)" role="img" aria-label="Photo looking up at city office towers against a blue sky"/>
  </svg>

  <div class="brand">
    <div class="brand-name">Levelpay</div>
    <div class="brand-sub">Merchant Services</div>
  </div>

  <div class="tagline">
    <div class="l1">Cutting Your</div>
    <div class="l2">Transaction <b>Costs</b></div>
    <div class="l3">INNOVATIVE PAYMENT SOLUTIONS</div>
  </div>

  <div class="quote-badge">
    <span class="small">WE WILL BEAT</span>
    <span class="big">ANY</span>
    <span class="small">LIKE FOR LIKE<br>QUOTE</span>
  </div>

  <ul class="usp-list">
    <li class="usp">
      <span class="usp-icon"><svg viewBox="0 0 34 34"><rect x="12" y="5" width="12" height="4" fill="#124c8c"/><rect x="12" y="11" width="12" height="4" fill="#124c8c"/><rect x="12" y="17" width="12" height="4" fill="#124c8c"/><path d="M4 22 h8 l8 4 h8 v3 H12 l-8-2z" fill="none" stroke="#124c8c" stroke-width="2"/></svg></span>
      <span>SAME DAY/NEXT<br>DAY FUNDING</span>
    </li>
    <li class="usp">
      <span class="usp-icon"><svg viewBox="0 0 34 34"><circle cx="13" cy="13" r="10" fill="#124c8c"/><text x="13" y="17" font-size="10" fill="#fff" text-anchor="middle" font-family="Roboto, sans-serif">24</text><path d="M18 18 l8 8 M22 18 l6 8" stroke="#124c8c" stroke-width="2" fill="none"/></svg></span>
      <span>24 HOUR<br>SWAP-OUT</span>
    </li>
    <li class="usp">
      <span class="usp-icon"><svg viewBox="0 0 34 34"><rect x="3" y="8" width="28" height="20" rx="3" fill="#124c8c"/><rect x="18" y="14" width="13" height="8" fill="#fff"/><circle cx="22" cy="18" r="1.8" fill="#124c8c"/></svg></span>
      <span>ORCHARD PAY &amp;<br>GALLOP PAY ENABLE</span>
    </li>
    <li class="usp">
      <span class="usp-icon"><svg viewBox="0 0 34 34"><rect x="8" y="3" width="16" height="24" rx="2" fill="none" stroke="#124c8c" stroke-width="2"/><rect x="11" y="7" width="10" height="10" fill="#124c8c"/><path d="M18 20 v10 h8 v-6 z" fill="#fff" stroke="#124c8c" stroke-width="1.5"/></svg></span>
      <span>INTERGRATED<br>EPOS SOLUTION</span>
    </li>
    <li class="usp">
      <span class="usp-icon"><svg viewBox="0 0 34 34"><ellipse cx="17" cy="20" rx="11" ry="8" fill="#124c8c"/><rect x="10" y="25" width="4" height="5" fill="#124c8c"/><rect x="20" y="25" width="4" height="5" fill="#124c8c"/><circle cx="17" cy="6" r="2.5" fill="#124c8c"/></svg></span>
      <span>SAVE UO TO 40%</span>
    </li>
  </ul>

  <div class="service service--epos">
    <div class="service-art art-epos" role="img" aria-label="Till screen, cash drawer and receipt printer"></div>
    EPOS<br>SYSTEMS
  </div>
  <div class="service service--cash">
    <div class="service-art art-cash" role="img" aria-label="Bundles of banknotes"></div>
    CASH<br>ADVANCE
  </div>
  <div class="service service--card">
    <div class="service-art art-card" role="img" aria-label="Card payment terminal"></div>
    CARD<br>PAYMENMTS
  </div>

  <div class="payment-row" aria-label="Accepted payment methods">
    <span class="pay-mark pay-mark--round"></span>
    <span class="pay-mark"></span>
    <span class="pay-mark"></span>
    <span class="pay-mark"></span>
    <span class="pay-mark pay-mark--purple"></span>
    <span class="pay-mark pay-mark--red"></span>
    <span class="pay-mark pay-mark--red"></span>
  </div>
</div>
</body>
</html>
```